exclusive Speakeasy Bar Web design in New Jersey USA

We are opening a speakeasy in New Jersey USA soon. we are looking for a web designer to do our web site including the coding. we a looking for a 4 to 5 page web design. the site will be mostly static. home page, contact page, menu page and a link to a 3rd party site (most likely Qelmo) for reservations. we are looking for this designer to do our menu deign as well. we are looking for a quick turnaround 7-10 days. i am attaching some pictures for the designers to see the concept design and the actual current pictures with our logo as well. professionally taken pictures will be provided later on. our photographer will be taking the pictures in the next week.

Industry/Entity Type

Restaurant, Bar, Speakeasy

Coding

Coded - Design and coding required

Number of Pages Required

4 page

Requirements
Must have
• home page, contact page, menu page and a link to qelmo.com for reservations
Nice to have
• some videos

```html
<!DOCTYPE html>
<html lang="en">
<head>
<meta charset="utf-8">
<title>217 Lounge — Speakeasy</title>
<link href="https://fonts.googleapis.com/css2?family=Poppins:wght@400;500;600;700;800&display=swap" rel="stylesheet">
<style>
:root{
  --ink:#2f3531;
  --ink-deep:#252a27;
  --sand:#dcc7a6;
  --sand-light:#e6d5b8;
  --tan:#d6bf99;
  --white:#ffffff;
  --muted:#cfc8bb;
}
*{margin:0;padding:0;box-sizing:border-box}
html,body{width:1200px;height:3446px;overflow:hidden}
body{position:relative;font-family:'Poppins',sans-serif;background:var(--sand);color:var(--ink)}
.abs{position:absolute}
.photo{position:absolute}
.btn{position:absolute;display:flex;align-items:center;justify-content:center;background:var(--white);color:var(--ink);font-size:17px;font-weight:400;letter-spacing:.2px;text-decoration:none}
.btn svg{position:absolute;left:-8px;top:0;height:100%}
.hero{left:0;top:0;width:1200px;height:685px;background:linear-gradient(180deg,#3d3a33 0%,#2c2924 45%,#1d1c1a 100%)}
.nav{right:0;top:32px;width:491px;height:48px;background:rgba(70,70,66,.85);display:flex;align-items:center;gap:58px;padding-left:75px}
.nav a{color:var(--tan);font-size:15px;font-weight:600;text-decoration:none}
.brand{left:110px;top:24px;width:70px;height:86px;border:2px solid #b89a6a;display:flex;align-items:center;justify-content:center;text-align:center;color:var(--ink);background:var(--sand-light);font-size:13px;font-weight:600;line-height:1.2}
.hero-card{left:237px;top:247px;width:733px;height:302px;background:rgba(74,73,64,.93);border-left:20px solid rgba(160,150,125,.55);border-right:20px solid rgba(160,150,125,.55);text-align:center}
.hero-card .pre{margin-top:35px;font-size:50px;font-weight:800;color:var(--white);line-height:1}
.hero-card .name{margin-top:6px;font-size:94px;font-weight:800;color:var(--tan);line-height:1}
h2{font-weight:800;font-size:42px;letter-spacing:.5px}
.about{left:0;top:685px;width:1200px;height:620px;background:var(--ink)}
.about h2{position:absolute;left:660px;top:110px;width:395px;text-align:center;color:var(--tan)}
.copy{font-size:15px;line-height:30px;text-align:justify;text-align-last:right;hyphens:auto}
.about .copy{position:absolute;left:626px;top:200px;width:462px;color:var(--muted)}
.section-title{left:0;width:1180px;text-align:center}
.card-title{font-size:14.5px;font-weight:600;text-align:center;width:340px}
.click{font-size:14.5px;font-weight:600;text-decoration:underline;text-align:center;width:200px}
.tag{position:absolute;bottom:10px;color:var(--white);font-size:15px}
.form-label{left:595px;color:var(--muted);font-size:17px}
.field{left:597px;width:441px;height:55px;background:rgba(220,199,166,.5)}
.footer{left:0;top:3131px;width:1200px;height:315px;background:linear-gradient(180deg,#2d302c,#1f211f)}
.fnav{display:flex;gap:70px}
.fnav a{color:var(--white);font-size:15px;font-weight:600;text-decoration:none}
</style>
</head>
<body>

<section class="abs hero">
  <div class="photo" role="img" aria-label="Backlit bar shelves lined with liquor bottles above a row of beer taps and glassware" style="left:0;top:0;width:1200px;height:685px;background:radial-gradient(ellipse at 15% 20%,rgba(210,190,160,.45),transparent 45%),linear-gradient(180deg,#4a4338 0%,#2f2a24 55%,#1b1a18 100%)"></div>
  <div class="abs brand">217<br>LOUNGE</div>
  <nav class="abs nav"><a>HOME</a><a>MENU</a><a>CONTACT</a></nav>
  <div class="abs hero-card">
    <div class="pre">WELCOME TO</div>
    <div class="name">217 LOUNGE</div>
  </div>
  <a class="btn" style="left:524px;top:466px;width:162px;height:42px">
    <svg viewBox="0 0 34 42"><polygon points="0,0 34,21 0,42" fill="#dcc7a6"/></svg>BOOK NOW</a>
  <svg class="abs" style="left:0;top:650px" width="1200" height="36"><polygon points="0,36 1200,0 1200,36" fill="#2f3531"/><polygon points="560,36 1200,8 1200,14 700,36" fill="#dcc7a6"/></svg>
</section>

<section class="abs about">
  <div class="abs" style="left:0;top:122px;width:549px;height:404px;background:var(--sand)"></div>
  <svg class="abs" style="left:0;top:122px" width="549" height="404"><polygon points="400,404 549,270 549,404" fill="#2f3531"/></svg>
  <div class="photo" role="img" aria-label="Lounge interior with tufted orange armchairs and a painted mural of cranes" style="left:0;top:122px;width:523px;height:368px;clip-path:polygon(0 0,100% 0,100% 72%,83% 100%,0 100%);background:linear-gradient(135deg,#3a3f3a 0%,#5a4a35 45%,#b8732e 65%,#7a5a3b 100%)"></div>
  <h2>ABOUT US</h2>
  <p class="copy" lang="en">Sed ut perspiciatis unde omnis iste natus error sit voluptatem accusantium doloremque laudantium, totam rem aperiam, eaque ipsa quae ab illo inventore veritatis et quasi architecto beatae vitae dicta sunt explicabo. Nemo enim ipsam voluptatem quia voluptas sit aspernatur aut odit aut fugit, sed quia consequuntur magni dolores eos qui ratione voluptatem sequi nesciunt. Neque porro quisquam est, qui dolorem ipsum quia dolor sit amet, consectetur</p>
  <a class="btn" style="left:784px;top:491px;width:165px;height:43px">
    <svg viewBox="0 0 34 43"><polygon points="0,0 34,21.5 0,43" fill="#dcc7a6"/></svg>READ MORE</a>
  <svg class="abs" style="left:0;top:572px" width="1200" height="48"><polygon points="0,0 870,48 0,48" fill="#ffffff"/></svg>
</section>

<h2 class="abs section-title" style="top:1418px">BOOK TONIGHT</h2>
<svg class="abs" style="left:40px;top:1630px" width="36" height="36"><circle cx="18" cy="18" r="15" fill="none" stroke="#2f3531" stroke-width="1.6"/><polyline points="21,11 14,18 21,25" fill="none" stroke="#2f3531" stroke-width="1.6"/></svg>
<svg class="abs" style="left:1124px;top:1630px" width="36" height="36"><circle cx="18" cy="18" r="15" fill="none" stroke="#2f3531" stroke-width="1.6"/><polyline points="15,11 22,18 15,25" fill="none" stroke="#2f3531" stroke-width="1.6"/></svg>

<div class="abs" style="left:83px;top:1523px;width:327px;height:294px;background:var(--ink);clip-path:polygon(0 0,100% 0,100% 100%,9% 100%,9% 10%)"></div>
<div class="photo" role="img" aria-label="Orange armchairs before a crane mural" style="left:111px;top:1523px;width:290px;height:286px;background:linear-gradient(140deg,#3c423c 0%,#55493a 45%,#b7722f 70%,#6e5439 100%)"><span class="tag" style="left:24px">$ 0.00</span><span class="tag" style="right:20px">★ 4.3</span></div>
<div class="abs card-title" style="left:96px;top:1830px">EMBER ROOM - HARBOR POINT</div>
<div class="abs click" style="left:146px;top:1883px">CLICK HERE</div>

<div class="abs" style="left:422px;top:1523px;width:325px;height:294px;background:var(--ink);clip-path:polygon(0 0,100% 0,100% 100%,9% 100%,9% 10%)"></div>
<div class="photo" role="img" aria-label="Mural wall with brass sconce above a covered booth" style="left:450px;top:1523px;width:289px;height:286px;background:linear-gradient(160deg,#4a4d45 0%,#6b6a5c 50%,#9a9a96 85%,#b5b3ad 100%)"><span class="tag" style="left:24px">$ 0.00</span><span class="tag" style="right:20px">★ 4.3</span></div>
<div class="abs card-title" style="left:425px;top:1830px">BRASS TABLE - ELM ROW</div>
<div class="abs click" style="left:490px;top:1883px">CLICK HERE</div>

<div class="abs" style="left:763px;top:1523px;width:326px;height:294px;background:var(--ink);clip-path:polygon(0 0,100% 0,100% 100%,9% 100%,9% 10%)"></div>
<div class="photo" role="img" aria-label="Bar room with globe pendant lights, orange chairs and a checkered floor" style="left:791px;top:1523px;width:289px;height:286px;background:linear-gradient(150deg,#2a2e2c 0%,#3f4a4a 40%,#a9733f 70%,#6a6f6e 100%)"><span class="tag" style="left:24px">$ 0.00</span><span class="tag" style="right:20px">★ 4.3</span></div>
<div class="abs card-title" style="left:766px;top:1830px">BRASS TABLE - ELM ROW</div>
<div class="abs click" style="left:833px;top:1883px">CLICK HERE</div>

<svg class="abs" style="left:0;top:1950px" width="1200" height="50"><polygon points="0,50 1200,0 1200,50" fill="#2f3531"/></svg>
<section class="abs" style="left:0;top:1996px;width:1200px;height:600px;background:var(--ink)">
  <div class="photo" role="img" aria-label="Dimly lit bar interior with pendant lights, brick wall and checkered floor" style="left:0;top:0;width:1200px;height:600px;background:linear-gradient(180deg,#2b302e 0%,#34403f 45%,#3c4a48 75%,#565b57 100%);opacity:.95"></div>
  <div class="abs" style="left:94px;top:115px;width:390px;height:485px;background:#545650;border-radius:195px 195px 0 0"></div>
  <div class="photo" role="img" aria-label="Bar counter under plastic sheeting with globe pendant lights overhead" style="left:111px;top:150px;width:353px;height:450px;border-radius:176px 176px 0 0;background:linear-gradient(180deg,#2f3d40 0%,#40585a 40%,#9a6b4f 65%,#8a5f47 85%,#2d4f52 100%)"></div>
  <h2 class="abs" style="left:620px;top:86px;width:392px;text-align:center;color:var(--white)">BOOK NOW</h2>
</section>
<div class="abs form-label" style="top:2168px">Name*</div>
<div class="abs field" style="top:2197px"></div>
<div class="abs form-label" style="top:2270px">Email Address*</div>
<div class="abs field" style="top:2304px"></div>
<div class="abs form-label" style="top:2377px">Contact Numaber*</div>
<div class="abs field" style="top:2406px"></div>
<a class="btn" style="left:720px;top:2494px;width:164px;height:42px">
  <svg viewBox="0 0 34 42"><polygon points="0,0 34,21 0,42" fill="#dcc7a6"/></svg>BOOK NOW</a>
<svg class="abs" style="left:0;top:2532px" width="1200" height="65"><polygon points="0,5 560,65 0,65" fill="#ffffff"/></svg>

<h2 class="abs" style="left:108px;top:2697px;width:415px;text-align:center">VIDEOS</h2>
<p class="abs copy" lang="en" style="left:108px;top:2785px;width:463px;color:var(--ink);text-align-last:left">Sed ut perspiciatis unde omnis iste natus error sit voluptatem accusantium doloremque laudantium, totam rem aperiam, eaque ipsa quae ab illo inventore veritatis et quasi architecto beatae vitae dicta sunt explicabo. Nemo enim ipsam voluptatem quia voluptas sit aspernatur aut odit aut fugit, sed quia consequuntur magni dolores eos qui ratione voluptatem sequi nesciunt. Neque porro quisquam est, qui dolorem ipsum quia dolor sit amet, consectetur</p>
<div class="abs" style="left:650px;top:2712px;width:414px;height:339px;background:var(--ink)"></div>
<div class="photo" role="img" aria-label="Video still of the bar under construction with teal-lit counter and stools" style="left:674px;top:2691px;width:414px;height:338px;background:linear-gradient(180deg,#2a2c2b 0%,#4a4a45 40%,#1f8a86 62%,#5a5650 80%,#8a8a88 100%)"></div>
<div class="abs" style="left:995px;top:2661px;width:121px;height:122px;background:var(--ink)"></div>
<svg class="abs" style="left:857px;top:2824px" width="68" height="68"><circle cx="34" cy="34" r="33" fill="#e2313f"/><polygon points="26,20 50,34 26,48" fill="#ffffff"/></svg>
<svg class="abs" style="left:1140px;top:2864px" width="22" height="26"><polyline points="6,3 16,13 6,23" fill="none" stroke="#2f3531" stroke-width="2.2"/></svg>

<footer class="abs footer">
  <div class="photo" role="img" aria-label="Faint backdrop of shelved liquor bottles" style="left:0;top:0;width:1200px;height:278px;background:radial-gradient(ellipse at 15% 30%,rgba(200,190,170,.35),transparent 40%),linear-gradient(180deg,#34352f,#232521)"></div>
  <div class="abs" style="left:107px;top:43px;width:147px;height:194px;border:2px solid #b89a6a;display:flex;align-items:center;justify-content:center;text-align:center;color:var(--ink);background:rgba(220,210,190,.85);font-size:22px;font-weight:600;line-height:1.3">217<br>LOUNGE</div>
  <div class="abs" style="left:340px;top:22px;display:flex;gap:16px">
    <span style="width:24px;height:24px;background:var(--white);border-radius:4px"></span>
    <span style="width:24px;height:24px;background:var(--white);border-radius:4px"></span>
    <span style="width:24px;height:24px;background:var(--white);border-radius:4px"></span>
    <span style="width:24px;height:24px;background:var(--white);border-radius:4px"></span>
  </div>
  <nav class="abs fnav" style="left:777px;top:23px"><a>HOME</a><a>MENU</a><a>CONTACT</a></nav>
  <div class="abs" style="left:341px;top:104px;color:var(--white);font-size:19px;font-weight:700">NEWSLETTER SUBSCRIBE</div>
  <div class="abs" style="left:339px;top:150px;width:206px;height:51px;background:var(--white);color:var(--ink);font-size:15px;padding:15px 0 0 18px">Email</div>
  <div class="abs" style="left:545px;top:150px;width:93px;height:51px;background:var(--sand);color:var(--ink);font-size:15px;font-weight:600;text-align:center;padding-top:14px">JOIN</div>
  <div class="abs" style="left:846px;top:106px;color:var(--white);font-size:17px;font-weight:700">LOACTION</div>
  <div class="abs" style="left:846px;top:138px;color:var(--white);font-size:15.5px;line-height:30px">42 Alder Lane<br>Millbrook<br>+1 555 010 2217</div>
  <div class="abs" style="left:0;top:278px;width:1200px;height:37px;background:#3b3d39;color:var(--white);font-size:13px;text-align:center;padding-top:9px">© 2023 217 Lounge. Com All Rights Reserved.</div>
</footer>

</body>
</html>
```